The Artist is "Vorlo" and the title of the project is .19 I need front and back cover ...

The front cover will be the 2 bullets, instead of the "38 spl" I want it to say Vorlo. Instead of the "TRM" I want it to say .19.. the 2 parenthesis looking marks can stay. I want this to look as natural as possible. Like it came from the factory with those words engraved. I was the bullets to keep their same gritty dirty look, along with a clean white background. Very simple. The back cover will be either an enclosed picture of a single bullet hole and the track listing, I will submit the pictures. White is the theme. If the grey metal hole picture is used I want to to be made white with the tracklisting on the background. If another type is used I would like the tracklisting INSIDE the bullet hole. I want the font to look serious and not cartoonish. Right now my tracklisting is kind of changing, so if the artist would be willing to work with me that would be great.
Rap/Hip hop

```html
<!DOCTYPE html>
<html lang="en">
<head>
<meta charset="utf-8">
<title>Vorlo /.19 — Cover Front and Back</title>
<link rel="stylesheet" href="https://fonts.googleapis.com/css2?family=Barlow+Semi+Condensed:wght@700&family=Barlow:wght@400;500&family=Montserrat:wght@800&display=swap">
<style>
  :root {
    --board: #ffffff;
    --blue: #1b6fb6;
    --tan: #c89b66;
    --ink: #000000;
    --panel-edge: #d4d4d4;
    --shadow: rgba(0, 0, 0, 0.28);
    --brass-light: #e2c77a;
    --brass-mid: #bf9c48;
    --brass-dark: #7a5e24;
    --engrave: #6b5020;
  }
  * { margin: 0; padding: 0; box-sizing: border-box; }
  html, body { width: 1200px; height: 756px; overflow: hidden; background: var(--board); }
  .board { position: relative; width: 1200px; height: 756px; }

  .sheet-mark {
    position: absolute; left: 38px; top: 33px;
    font: 700 13px/1 "Barlow Semi Condensed", sans-serif; color: var(--blue);
  }
  .side-label {
    position: absolute; top: 101px; width: 200px; text-align: center;
    font: 700 14px/1 "Barlow Semi Condensed", sans-serif; letter-spacing: 0.03em; color: var(--blue);
  }
  .side-label--front { left: 248px; }
  .side-label--back { left: 779px; }

  .cover {
    position: absolute; top: 155px; width: 428px; height: 428px;
    background: var(--board); border: 1px solid var(--panel-edge);
    box-shadow: -10px 14px 12px -6px var(--shadow);
    overflow: hidden;
  }
  .cover--front { left: 126px; }
  .cover--back { left: 657px; }

  .front-photo {
    position: absolute; inset: 0;
    background: linear-gradient(152deg, #fbf8f1 0%, var(--brass-light) 30%, var(--brass-mid) 55%, var(--brass-dark) 72%, #f4efe6 100%);
  }
  .headstamp {
    position: absolute; left: 178px; top: 234px; width: 130px; height: 140px;
  }
  .headstamp text {
    font: 700 19px "Barlow Semi Condensed", sans-serif;
    fill: var(--engrave); letter-spacing: 2px;
  }

  .tracklist { position: absolute; left: 22px; top: 36px; list-style: none; }
  .track {
    display: grid; grid-template-columns: 15px 102px auto;
    height: 41.7px; align-items: start;
  }
  .track__no { font: 500 10px/14px "Barlow", sans-serif; color: var(--tan); }
  .track__title { font: 700 10.5px/14px "Barlow Semi Condensed", sans-serif; color: var(--blue); white-space: nowrap; }
  .track__time { font: 400 10px/14px "Barlow", sans-serif; color: var(--tan); }

  .imprint {
    position: absolute; left: 26px; top: 383px;
    font: 500 8.5px/12px "Barlow", sans-serif; letter-spacing: 0.06em; color: var(--tan);
  }

  .bullet-hole {
    position: absolute; left: 158px; top: 22px; width: 260px; height: 300px;
    background: radial-gradient(ellipse 46% 42% at 50% 46%, var(--ink) 0%, var(--ink) 68%, #9a9a9a 74%, #e4e4e4 86%, transparent 100%);
  }
  .album-title {
    position: absolute; left: 180px; top: 143px; width: 216px; text-align: center;
    font: 800 23px/1 "Montserrat", sans-serif; letter-spacing: 0.08em; color: var(--board);
  }
</style>
</head>
<body>
<main class="board">
  <span class="sheet-mark">B</span>
  <h2 class="side-label side-label--front">FRONT</h2>
  <h2 class="side-label side-label--back">BACK</h2>

  <section class="cover cover--front">
    <div class="front-photo" role="img" aria-label="Photograph of two gritty brass revolver cartridges on a clean white background, one lying across the other standing on its base"></div>
    <svg class="headstamp" viewBox="0 0 130 140" aria-label="Head stamp engraving VORLO .19">
      <defs>
        <path id="stamp-top" d="M 14 70 A 52 52 0 0 1 116 70"/>
        <path id="stamp-bottom" d="M 20 76 A 46 46 0 0 0 110 76"/>
      </defs>
      <text><textPath href="#stamp-top" startOffset="50%" text-anchor="middle">VORLO</textPath></text>
      <text><textPath href="#stamp-bottom" startOffset="50%" text-anchor="middle" dominant-baseline="hanging">.19</textPath></text>
    </svg>
  </section>

  <section class="cover cover--back">
    <ol class="tracklist">
      <li class="track"><span class="track__no">1.</span><span class="track__title">LOREM IPSUM DOLOR</span><span class="track__time">3:25</span></li>
      <li class="track"><span class="track__no">2.</span><span class="track__title">SIT AMET</span><span class="track__time">10:24</span></li>
      <li class="track"><span class="track__no">3</span><span class="track__title">CONSECTETUER ADIP</span><span class="track__time">5:20</span></li>
      <li class="track"><span class="track__no">4.</span><span class="track__title">SED DIAM NONUMMY</span><span class="track__time">8:38</span></li>
      <li class="track"><span class="track__no">5.</span><span class="track__title">NIBH EUISMOD TINCID</span><span class="track__time">5:33</span></li>
      <li class="track"><span class="track__no">6.</span><span class="track__title">UT LAOREET DOLORE</span><span class="track__time">2:58</span></li>
      <li class="track"><span class="track__no">7.</span><span class="track__title">MAGNA ALIQUAM ERAT</span><span class="track__time">3:30</span></li>
      <li class="track"><span class="track__no">8.</span><span class="track__title">TATION</span><span class="track__time">6:50</span></li>
    </ol>

    <div class="bullet-hole" role="img" aria-label="Illustration of a bullet hole torn through white paper, black opening in the centre"></div>
    <h1 class="album-title">VORLO /.19</h1>

    <p class="imprint">®2020 - VORLO STUDIOS<br>USA NEVADA. PO BOX. 2210-C</p>
  </section>
</main>
</body>
</html>
```